Corvane Capital LLC
I need single sided standard sized Business Card [3.5" x 2"]
Fonts to be determined by designer
Professional
Derek Halloway
Chairman
Kestrel Hall Tower
418 North Larkin Avenue
Los Angeles, CA 90099
555.014.2739 X1
Acquisitions@Corvane-Capital.net
http://www.Corvane-Capital.net
We want to see what designs are out there for a cutting edge business card that shows off our 3 main goals: Intense - Expressive - Important . The business card can be vertical or horizontal, can use fonts of the designer's choice and be relatively "unique". More than just a simple black on white business card.
Use the logo and CORVANE but you do not need to use the blue background if your design does not warrant it. Financial LLC can be in any font you desire if it matches your design

```html
<!DOCTYPE html>
<html lang="en">
<head>
<meta charset="utf-8">
<title>Corvane Capital LLC – Business Card</title>
<link href="https://fonts.googleapis.com/css2?family=Open+Sans:wght@400;600;700&display=swap" rel="stylesheet">
<style>
  :root {
    --backdrop: #6a3220;
    --card-white: #ffffff;
    --gold-light: #d2a83c;
    --gold-mid: #a9771e;
    --gold-deep: #6e4310;
    --swoosh: #161616;
    --brand: #9a6a1d;
    --brand-sub: #5a3a12;
    --mark: #2b2b2b;
    --text-light: #ffffff;
  }
  * { margin: 0; padding: 0; box-sizing: border-box; }
  html, body {
    width: 1200px;
    height: 965px;
    overflow: hidden;
    background: var(--backdrop);
    font-family: "Open Sans", Arial, sans-serif;
  }
  .stage {
    position: relative;
    width: 1200px;
    height: 965px;
  }
  .business-card {
    position: absolute;
    left: 215px;
    top: 262px;
    width: 770px;
    height: 440px;
    border-radius: 26px;
    overflow: hidden;
    background: var(--card-white);
  }
  .card-art {
    position: absolute;
    inset: 0;
    width: 770px;
    height: 440px;
  }
  .holder {
    position: absolute;
    left: 26px;
    top: 22px;
    color: var(--text-light);
  }
  .holder-name {
    font-weight: 700;
    font-size: 21px;
    line-height: 28px;
  }
  .holder-title {
    font-weight: 400;
    font-size: 19px;
    line-height: 26px;
  }
  .contact {
    position: absolute;
    left: 26px;
    top: 238px;
    color: var(--text-light);
    font-size: 16px;
    line-height: 22.5px;
    list-style: none;
  }
  .contact b { font-weight: 700; }
  .brand {
    position: absolute;
    left: 400px;
    top: 56px;
    width: 266px;
    text-align: center;
    color: var(--brand);
  }
  .brand-mark {
    display: block;
    width: 78px;
    height: 78px;
    margin: 0 auto 22px;
    background: var(--mark);
  }
  .brand-name {
    font-weight: 400;
    font-size: 46px;
    line-height: 50px;
    letter-spacing: 3px;
  }
  .brand-sub {
    font-weight: 400;
    font-size: 12px;
    line-height: 18px;
    letter-spacing: 6px;
    color: var(--brand);
  }
</style>
</head>
<body>
<main class="stage">
  <section class="business-card" aria-label="Corvane Capital LLC business card">
    <svg class="card-art" viewBox="0 0 770 440" aria-hidden="true">
      <defs>
        <radialGradient id="goldPanel" cx="0.45" cy="0.42" r="0.75">
          <stop offset="0" stop-color="var(--gold-light)"/>
          <stop offset="0.55" stop-color="var(--gold-mid)"/>
          <stop offset="1" stop-color="var(--gold-deep)"/>
        </radialGradient>
      </defs>
      <path class="swoosh" d="M215 0 H262 C 328 110, 372 330, 565 440 H540 C 330 335, 300 95, 232 0 Z" fill="var(--swoosh)"/>
      <path class="gold-panel" d="M0 0 H232 C 300 95, 330 335, 540 440 H0 Z" fill="url(#goldPanel)"/>
    </svg>

    <div class="holder">
      <p class="holder-name">Derek Halloway</p>
      <p class="holder-title">Chairman</p>
    </div>

    <ul class="contact">
      <li>Kestrel Hall Tower</li>
      <li>418 North Larkin Avenue</li>
      <li>Los Angeles, CA 90099</li>
      <li><b>Phone :</b> 555.014.2739 X1</li>
      <li><b>Fax :</b> 555.017.6021</li>
      <li><b>Email :</b> Acquisitions@Corvane-Capital.net</li>
      <li><b>Web :</b> http://www.Corvane-Capital.net</li>
    </ul>

    <div class="brand">
      <span class="brand-mark"></span>
      <p class="brand-name">CORVANE</p>
      <p class="brand-sub">CAPITAL LLC</p>
    </div>
  </section>
</main>
</body>
</html>
```